KVT Business Cards

We require business cards for our business. We would like a matte black back to the card, with our logo centred in the middle. The front side of the card is open to design.

Target Market(s)

Clients looking for legal services (professional)

Industry/Entity Type

Legal

Contact Information for Business Card

Boris Telemark
Partner
Mobile: 0438 715 642
Email: boris@kvtlaw.co
Website: www.kvtlaw.co
Level 3, 118 Wexbury Street
Sydney NSW 2000

Font styles to use
Other font styles liked:
• Avenir

Colors
f04a50
ffffff
1b1b1b

Requirements
Must have
• Black back with logo included in the centre of the card.
• Our font is Avenir.

```html
<!DOCTYPE html>
<html lang="en">
<head>
<meta charset="utf-8">
<title>KVT Legal – Business Cards</title>
<link href="https://fonts.googleapis.com/css2?family=Nunito+Sans:wght@400;600;800&display=swap" rel="stylesheet">
<style>
  :root {
    --stage: #161616;
    --card: #1e1e1e;
    --card-edge: #262626;
    --accent: #dc2250;
    --ink: #ffffff;
    --ink-soft: #e8e8e8;
  }
  * { box-sizing: border-box; margin: 0; padding: 0; }
  html, body {
    width: 1200px; height: 900px; overflow: hidden;
    background: var(--stage);
    font-family: "Nunito Sans", "Avenir", sans-serif;
  }
  .stage {
    width: 1200px; height: 900px;
    display: flex; flex-direction: column; align-items: center; justify-content: center;
    gap: 36px;
  }
  .card {
    position: relative;
    width: 700px; height: 400px;
    background: linear-gradient(135deg, var(--card-edge), var(--card) 60%);
    border-bottom: 6px solid var(--accent);
    box-shadow: 0 18px 40px rgba(0,0,0,.55);
  }
  .brand {
    display: flex; align-items: center; gap: 18px;
  }
  .brand-square {
    width: 46px; height: 46px; background: var(--accent);
  }
  .brand-name {
    color: var(--ink); font-weight: 800; font-size: 44px;
    letter-spacing: 1px; line-height: 1; text-transform: uppercase;
  }
  .card-back {
    display: flex; align-items: center; justify-content: center;
  }
  .card-front .brand {
    position: absolute; left: 60px; top: 168px;
  }
  .card-front .brand-square { width: 40px; height: 40px; }
  .card-front .brand-name { font-size: 38px; }
  .divider {
    position: absolute; left: 370px; top: 88px;
    width: 2px; height: 210px; background: var(--accent);
  }
  .contact {
    position: absolute; left: 400px; top: 84px;
    color: var(--ink-soft); font-size: 18px; line-height: 1.35;
  }
  .person-name {
    color: var(--accent); font-weight: 800; font-size: 25px;
    text-transform: uppercase; letter-spacing: .5px; line-height: 1.1;
  }
  .person-role { font-size: 18px; margin-bottom: 16px; letter-spacing: .5px; }
  .address { margin-bottom: 14px; }
  .contact-line { display: flex; align-items: center; gap: 10px; }
  .contact-line svg { width: 13px; height: 13px; flex: none; }
</style>
</head>
<body>
<main class="stage">
  <section class="card card-back" aria-label="Card back">
    <div class="brand">
      <span class="brand-square"></span>
      <span class="brand-name">KVT Legal</span>
    </div>
  </section>

  <section class="card card-front" aria-label="Card front">
    <div class="brand">
      <span class="brand-square"></span>
      <span class="brand-name">KVT Legal</span>
    </div>
    <span class="divider"></span>
    <div class="contact">
      <p class="person-name">Boris Telemark</p>
      <p class="person-role">General Manager</p>
      <p class="address">Level 3, 118 Wexbury Street<br>Sydney NSW 2000</p>
      <p class="contact-line">
        <svg viewBox="0 0 16 16" aria-hidden="true"><path d="M3 1h3l1.5 4-2 1.3a9 9 0 0 0 4.2 4.2L11 8.5l4 1.5v3a2 2 0 0 1-2 2A13 13 0 0 1 1 3a2 2 0 0 1 2-2z" fill="var(--accent)"/></svg>
        0438 715 642
      </p>
      <p class="contact-line">
        <svg viewBox="0 0 16 16" aria-hidden="true"><rect x="1" y="3" width="14" height="10" fill="none" stroke="var(--accent)" stroke-width="1.6"/><path d="M1 3l7 6 7-6" fill="none" stroke="var(--accent)" stroke-width="1.6"/></svg>
        boris@kvtlaw.co
      </p>
      <p class="contact-line">
        <svg viewBox="0 0 16 16" aria-hidden="true"><circle cx="8" cy="8" r="6.5" fill="none" stroke="var(--accent)" stroke-width="1.5"/><ellipse cx="8" cy="8" rx="3" ry="6.5" fill="none" stroke="var(--accent)" stroke-width="1.2"/><path d="M1.5 8h13" stroke="var(--accent)" stroke-width="1.2"/></svg>
        www.kvtlaw.co
      </p>
    </div>
  </section>
</main>
</body>
</html>
```